PowerPoint Template Needed for Investment Firm

Meridale Capital Management is an emerging wealth management firm based in New Jersey. It offers superior investment returns to high net worth individuals and institutions by finding undervalued assets.

We recently selected a company logo which was inspired by the Meridale constellation. Beta Tucanae is a group of six stars, containing star cluster 47 Tucanae, rated the second brightest object in the sky.

Now we need a PowerPoint template with the designs for the following:

1. Title/cover page slide
2. Content slide with title
3. Section slide - to introduce a new section
4. Final slide - with contact information

The slides will be used at investor presentations, that is, to provide information about the company to potential investors. Since we are an investment firm, the design should project a sense of stability, growth and professionalism. The owner is interested in something simple yet striking, which of course is consistent with the logo. I'm thinking more conservative colors and Sans Serif fonts.

I plan on changing the status to non-refundable once I see some designs that I really like.

Target Market(s)

Wealthy individuals, probably middle aged or older, in the US

Industry/Entity Type

Conservative

Requirements
Must have
• Sans serif fonts
Clean, very professional look
Conservative colors that complement existing logo
Should not have
• Anything too busy or complicated

```html
<!DOCTYPE html>
<html lang="en">
<head>
<meta charset="utf-8">
<title>Meridale Capital Management – Slide Template</title>
<link rel="stylesheet" href="https://fonts.googleapis.com/css2?family=PT+Sans:wght@400;700&display=swap">
<style>
:root{
  --navy:#1f3590;
  --ink:#3d4557;
  --brand:#3b4560;
  --body:#4a4a4a;
  --band-grey:#6d6e70;
  --band-blue:#2b3f9e;
  --stage:#e9e6e1;
  --paper:#ffffff;
}
*{box-sizing:border-box;margin:0;padding:0}
html,body{width:1200px;height:458px;overflow:hidden;background:var(--stage)}
body{font-family:"PT Sans",Arial,sans-serif;color:var(--body)}
.deck{position:relative;width:1200px;height:458px}
.slide{position:absolute;width:266px;height:200px;background:var(--paper);overflow:hidden;box-shadow:0 1px 3px rgba(0,0,0,.25)}
.col1{left:7px}.col2{left:311px}.col3{left:616px}.col4{left:928px}
.row1{top:5px}.row2{top:252px}
.footer-band{position:absolute;left:0;bottom:0;width:266px;height:7px}
.slide-title{position:absolute;left:13px;top:6px;font-size:11.5px;font-weight:700;color:var(--navy)}
.title-swoosh{position:absolute;left:13px;top:20px;width:92px;height:6px}
.brand-mini{position:absolute;right:10px;top:8px;font-size:5.5px;font-weight:700;color:var(--brand);white-space:nowrap}
.para{position:absolute;font-size:4.5px;line-height:1.35;color:var(--body)}
.bullets{position:absolute;list-style:none;font-size:5.2px;font-weight:700;color:var(--ink)}
.bullets li{position:relative;padding-left:9px;margin-bottom:4.4px}
.bullets li::before{content:"";position:absolute;left:0;top:.5px;width:5px;height:5px;border-radius:50%;background:var(--navy)}
.visual{position:absolute}
.brand-lockup{position:absolute;left:0;width:100%;display:flex;align-items:center;justify-content:center;gap:7px}
.brand-dot{width:14px;height:14px;border-radius:50%;background:var(--navy);flex:none}
.brand-name{font-size:14px;font-weight:700;color:var(--brand);white-space:nowrap}
.cover-title{position:absolute;left:0;width:100%;text-align:center;top:140px;font-size:17px;font-weight:700;color:var(--navy)}
.photo-slot{position:absolute;left:15px;top:29px;width:86px;height:66px;background:#c9c9c9;border:4px solid #e2e2e2;outline:1px solid #9a9a9a;display:flex;align-items:center;justify-content:center;text-align:center;font-size:12px;line-height:1.2;color:#111}
.subhead{font-size:5px;font-weight:700;color:var(--navy);margin-bottom:1.5px}
.subgroup{margin-bottom:10px}
.contact{position:absolute;left:0;width:100%;text-align:center;font-size:7px;font-weight:700;line-height:1.65}
.contact .addr{color:var(--ink)}
.contact .label{color:var(--navy)}
.contact .value{color:var(--ink)}
</style>
</head>
<body>
<main class="deck">

  <section class="slide col1 row1">
    <div class="brand-lockup" style="top:92px"><span class="brand-dot"></span><span class="brand-name">Meridale Capital Management</span></div>
    <h1 class="cover-title">Presentation Title</h1>
    <svg class="footer-band" viewBox="0 0 266 7"><polygon points="0,0 146,0 140,7 0,7" fill="var(--band-grey)"/><polygon points="150,0 266,0 266,7 144,7" fill="var(--band-blue)"/></svg>
  </section>

  <section class="slide col2 row1">
    <h2 class="slide-title">Investment Strategy</h2>
    <svg class="title-swoosh" viewBox="0 0 92 6"><path d="M0,4 Q46,0 92,4" stroke="var(--navy)" stroke-width="1" fill="none"/></svg>
    <div class="brand-mini">Meridale Capital Management</div>
    <div class="visual" role="img" aria-label="Photo of a pen over a printed blue pie chart report" style="left:0;top:60px;width:266px;height:133px;background:linear-gradient(160deg,#ffffff 10%,#dde6f3 45%,#7ea3d8 70%,#e9eef6 95%)"></div>
    <p class="para" style="left:13px;top:30px;width:240px">Lorem ipsum d olor sit amet, consectetuer adipiscing elit, sed diam nonummy nibh euismod tincidunt ut laoreet dolore magna aliquam erat volutpat. Ut wisi enim ad minim veniam, quis nostrud exerci tation ullamcorper suscipit lobortis nisl ut aliquip ex ea commodo consequat. Duis autem vel eum iriure dolor in hendrerit in vulputate velit esse molestie consequat, vel illum dolore eu feugiat nulla facilisis.</p>
    <ul class="bullets" style="left:13px;top:80px"><li>Lorem ipsum Lorem Lorem ipsum Lorem Lorem ipsum</li><li>Lorem ipsum Lorem Lorem Lorem ipsum</li><li>Lorem ipsum Lorem Lorem ipsum Lorem Lorem ips</li></ul>
    <svg class="footer-band" viewBox="0 0 266 7"><polygon points="0,0 146,0 140,7 0,7" fill="var(--band-grey)"/><polygon points="150,0 266,0 266,7 144,7" fill="var(--band-blue)"/></svg>
  </section>

  <section class="slide col3 row1">
    <h2 class="slide-title">Financial Returns</h2>
    <svg class="title-swoosh" viewBox="0 0 92 6"><path d="M0,4 Q46,0 92,4" stroke="var(--navy)" stroke-width="1" fill="none"/></svg>
    <div class="brand-mini">Meridale Capital Management</div>
    <p class="para" style="left:13px;top:30px;width:240px">Lorem ipsum d olor sit amet, consectetuer adipiscing elit, sed diam nonummy nibh euismod tincidunt ut laoreet dolore magna aliquam erat volutpat. Ut wisi enim ad minim veniam, quis nostrud exerci tation ullamcorper suscipit lobortis nisl ut aliquip ex ea commodo consequat. Duis autem vel eum iriure dolor in hendrerit in vulputate velit esse molestie consequat, vel illum dolore eu feugiat nulla facilisis.</p>
    <ul class="bullets" style="left:13px;top:78px"><li>Lorem ipsum Lorem Lorem ipsum Lorem Lorem ipsum</li><li>Lorem ipsum Lorem Lorem Lorem ipsum</li><li>Lorem ipsum Lorem Lorem ipsum Lorem Lorem ipsum</li><li>Lorem ipsum Lorem Lorem</li><li>Lorem ipsum Lorem Lorem ipsum</li><li>Lorem ipsum orem Lorem Lo</li><li>Lorem ipsum Lorem Lore</li></ul>
    <div class="visual" role="img" aria-label="Photo of a cheerful businessman holding banknotes in both hands" style="left:140px;top:115px;width:126px;height:78px;background:linear-gradient(180deg,#ffffff 0%,#cfdff2 40%,#3f7fcf 100%)"></div>
    <svg class="footer-band" viewBox="0 0 266 7"><polygon points="0,0 146,0 140,7 0,7" fill="var(--band-grey)"/><polygon points="150,0 266,0 266,7 144,7" fill="var(--band-blue)"/></svg>
  </section>

  <section class="slide col4 row1">
    <h2 class="slide-title">Manager Biography</h2>
    <svg class="title-swoosh" viewBox="0 0 92 6"><path d="M0,4 Q46,0 92,4" stroke="var(--navy)" stroke-width="1" fill="none"/></svg>
    <div class="brand-mini">Meridale Capital Management</div>
    <div class="photo-slot">Your Photo<br>Here</div>
    <p class="para" style="left:107px;top:30px;width:148px">Lorem ipsum d olor sit amet, consectetuer adipiscing elit, sed diam nonummy nibh euismod tincidunt ut laoreet dolore magna aliquam erat volutpat. Ut wisi enim ad minim veniam, quis nostrud exerci tation ullamcorper suscipit lobortis nisl ut aliquip ex ea commodo consequat. Duis autem vel eum iriure dolor in hendrerit in vulputate velit esse molestie consequat, vel illum dolore eu feugiat nulla facilisis.</p>
    <ul class="bullets" style="left:13px;top:102px"><li>Lorem ipsum Lorem Lorem ipsum Lorem Lorem ipsum</li><li>Lorem ipsum Lorem Lorem Lorem Lorem ipsum</li><li>Lorem ipsum Lorem Lorem ipsum Lorem Lorem ipsum</li></ul>
    <p class="para" style="left:13px;top:137px;width:240px">Lorem ipsum d olor sit amet, consectetuer adipiscing elit, sed diam nonummy nibh euismod tincidunt ut laoreet dolore magna aliquam erat volutpat. Ut wisi enim ad minim veniam, quis nostrud exerci tation ullamcorper suscipit lobortis nisl ut aliquip ex ea commodo consequat. Duis autem vel eum iriure dolor in hendrerit in vulputate velit esse molestie conseq.</p>
    <svg class="footer-band" viewBox="0 0 266 7"><polygon points="0,0 146,0 140,7 0,7" fill="var(--band-grey)"/><polygon points="150,0 266,0 266,7 144,7" fill="var(--band-blue)"/></svg>
  </section>

  <section class="slide col1 row2">
    <h2 class="slide-title">Lorem Ipsum</h2>
    <svg class="title-swoosh" viewBox="0 0 92 6"><path d="M0,4 Q46,0 92,4" stroke="var(--navy)" stroke-width="1" fill="none"/></svg>
    <div class="brand-mini">Meridale Capital Management</div>
    <p class="para" style="left:13px;top:30px;width:240px">Lorem ipsum d olor sit amet, consectetuer adipiscing elit, sed diam nonummy nibh euismod tincidunt ut laoreet dolore magna aliquam erat volutpat. Ut wisi enim ad minim veniam, quis nostrud exerci tation ullamcorper suscipit lobortis nisl ut aliquip ex ea commodo consequat. Duis autem vel eum iriure dolor in hendrerit in vulputate velit esse molestie consequat, vel illum dolore eu feugiat nulla facilisis.</p>
    <div class="visual" role="img" aria-label="Illustration of a profit, loss and return gauge with figures and a briefcase" style="left:10px;top:77px;width:115px;height:110px;background:radial-gradient(ellipse at 45% 45%,#f4ecc4 0%,#e7d89a 45%,#ffffff 72%)"></div>
    <p class="para" style="left:140px;top:77px;width:115px">Lorem ipsum d olor sit amet, consectetuer adipiscing elit, sed diam nonummy nibh euismod tincidunt ut laoreet dolore magna aliquam erat volutpat. Ut wisi enim ad minim veniam, quis nostrud exerci tation.</p>
    <p class="para" style="left:140px;top:126px;width:115px">Lorem ipsum d olor sit amet, consectetuer adipiscing elit, sed diam nonummy nibh euismod tincidunt ut laoreet dolore magna aliquam erat volutpat. Ut wisi enim ad minim veniam, quis nostrud exerci tation.</p>
    <svg class="footer-band" viewBox="0 0 266 7"><polygon points="0,0 146,0 140,7 0,7" fill="var(--band-grey)"/><polygon points="150,0 266,0 266,7 144,7" fill="var(--band-blue)"/></svg>
  </section>

  <section class="slide col2 row2">
    <h2 class="slide-title">Lorem Ipsum</h2>
    <svg class="title-swoosh" viewBox="0 0 92 6"><path d="M0,4 Q46,0 92,4" stroke="var(--navy)" stroke-width="1" fill="none"/></svg>
    <div class="brand-mini">Meridale Capital Management</div>
    <p class="para" style="left:13px;top:30px;width:240px">Lorem ipsum d olor sit amet, consectetuer adipiscing elit, sed diam nonummy nibh euismod tincidunt ut laoreet dolore magna aliquam erat volutpat. Ut wisi enim ad minim veniam, quis nostrud exerci tation ullamcorper suscipit lobortis nisl ut aliquip ex ea commodo consequat. Duis autem vel eum iriure dolor in hendrerit in vulputate velit esse molestie consequat, vel illum dolore eu feugiat nulla facilisis.</p>
    <p class="para" style="left:13px;top:77px;width:118px">Lorem ipsum d olor sit amet, consectetuer adipiscing elit, sed diam nonummy nibh euismod tincidunt ut laoreet dolore magna aliquam erat volutpat. Ut wisi enim ad minim veniam, quis nostrud exerci tation.</p>
    <p class="para" style="left:13px;top:126px;width:118px">Lorem ipsum d olor sit amet, consectetuer adipiscing elit, sed diam nonummy nibh euismod tincidunt ut laoreet dolore magna aliquam erat volutpat. Ut wisi enim ad minim veniam, quis nostrud exerci tation.</p>
    <div class="visual" role="img" aria-label="Photo of a heap of dollar banknotes" style="left:138px;top:92px;width:124px;height:96px;background:radial-gradient(ellipse at 55% 55%,#6f7a66 0%,#aab3a1 45%,#ffffff 75%)"></div>
    <svg class="footer-band" viewBox="0 0 266 7"><polygon points="0,0 146,0 140,7 0,7" fill="var(--band-grey)"/><polygon points="150,0 266,0 266,7 144,7" fill="var(--band-blue)"/></svg>
  </section>

  <section class="slide col3 row2">
    <h2 class="slide-title">Lorem Ipsum</h2>
    <svg class="title-swoosh" viewBox="0 0 92 6"><path d="M0,4 Q46,0 92,4" stroke="var(--navy)" stroke-width="1" fill="none"/></svg>
    <div class="brand-mini">Meridale Capital Management</div>
    <div class="para" style="left:13px;top:33px;width:113px">
      <div class="subgroup"><p class="subhead">Sub Title-1</p><p>Lorem ipsum dolor sit amet, etuer.Lorem ipsum dolor sit amet, etuer.Lorem ipsum dolor sit amet, etuer.Lorem ipsum dolor sit</p></div>
      <div class="subgroup"><p class="subhead">Sub Title-2</p><p>Lorem ipsum dolor sit amet, etuer.Lorem ipsum dolor sit amet, etuer.Lorem ipsum dolor sit amet, etuer.Lorem ipsum dolor sit</p></div>
      <div class="subgroup"><p class="subhead">Sub Title-3</p><p>Lorem ipsum dolor sit amet, etuer.Lorem ipsum dolor sit amet, etuer.Lorem ipsum dolor sit amet, etuer.Lorem ipsum dolor sit</p></div>
    </div>
    <div class="para" style="left:144px;top:33px;width:113px">
      <div class="subgroup"><p class="subhead">Sub Title-1</p><p>Lorem ipsum dolor sit amet, etuer.Lorem ipsum dolor sit amet, etuer.Lorem ipsum dolor sit amet, etuer.Lorem ipsum dolor sit</p></div>
      <div class="subgroup"><p class="subhead">Sub Title-2</p><p>Lorem ipsum dolor sit amet, etuer.Lorem ipsum dolor sit amet, etuer.Lorem ipsum dolor sit amet, etuer.Lorem ipsum dolor sit</p></div>
      <div class="subgroup"><p class="subhead">Sub Title-3</p><p>Lorem ipsum dolor sit amet, etuer.Lorem ipsum dolor sit amet, etuer.Lorem ipsum dolor sit amet, etuer.Lorem ipsum dolor sit</p></div>
    </div>
    <svg class="footer-band" viewBox="0 0 266 7"><polygon points="0,0 146,0 140,7 0,7" fill="var(--band-grey)"/><polygon points="150,0 266,0 266,7 144,7" fill="var(--band-blue)"/></svg>
  </section>

  <section class="slide col4 row2">
    <div class="brand-lockup" style="top:82px"><span class="brand-dot"></span><span class="brand-name">Meridale Capital Management</span></div>
    <div class="contact" style="top:136px">
      <p class="addr">45 Harbor Ave. Newark, NJ 07102</p>
      <p><span class="label">Phone:</span> <span class="value">555-010-2480</span></p>
      <p><span class="label">Email:</span> <span class="value">info@meridalecapmgmt.com</span></p>
    </div>
    <svg class="footer-band" viewBox="0 0 266 7"><polygon points="0,0 146,0 140,7 0,7" fill="var(--band-grey)"/><polygon points="150,0 266,0 266,7 144,7" fill="var(--band-blue)"/></svg>
  </section>

</main>
</body>
</html>
```